We need a design for our website called Mivelda which is a brazilian e-commerce focused on childrenswear. Basically your are able to swap (sell & buy) your kids outgrown clothes in the website and we will offer all the necessary services to help you on that.

We believe the main characteristic of the company is the swap of clothes and accessories, but we also feel that by doing this we are guaranteeing that this clothes are not going to trash, reducing clothes waste and being friendly with the environment.

We believe it should be clean with solid and soft colors (refer to the logo attached) and should communicate high quality standards and trust.

We need 2 web pages: home/search results and product details. In both pages we would like to have a fixed top bar with the logo, menu (Buy, Sell, About Us), login, a short message and shopping cart. As well as a footer on the botton with different options and social network links.

- Home/search results: right at the beginning of the page we would like to have a welcome/explanatory carousel banner. It should be a conventional 2 columns design with filters on the left (~25%) and the results on the main section (~3/4 products per row). We need filters for clothes and accessories (size,category, brands, color, gender).

- Product details: again, this should be very clean, with breadcrumbs on the top, a very short description (product's name, category, size), price, "Add to cart" button, an image with zoom functionality (as reference: jquery jqzoom), a "Similar Items" box and a share bar (chatloom, quibbly, snapquilt, v+).

Please bear in mind that we plan to use the main template in different colors across the website.
Updates

Hi everyone! 

We have just updated the brief to add some "Must have features" and "Nice to have features". Please take a careful look at it as it affects pretty much every design we received so far.

We will guarantee the project in the next 1-2 days, but we first would like to see some initial proposals for the second page (product details). Some of you guys are doing an awesome job in the home page!

Best,

Mivelda team

We have just updated the contest payment status: it is now committed!

Best,
Mivelda Team

Target Market(s)

The main audience will be parents of any age

Industry/Entity Type

E-Commerce

Requirements
Must have
• We would like to have only the following elements in the header: logo, login, cart image, Home, "Compre" (Buy), "Venda" (Sell) - not necessarily in this order
- The header should be persistent all over the website (always fixed at the top), thus, if it is too thick it will end up eating too much vertical space in some pages
- The current page should be somehow highlited in the header
- Right next to the cart image on the top we need a small tag indicating how many itens are already inside the cart
- We need a button "Entenda como funcionamos" (which in english means "Learn more") in the banner
- Please use an image of childrens in the banner (not clothes or teenagers)
- Besides the banner, the user in a1024x768 screen resolution should at least be able to view the first row of search results
- There is no need for a "Add to cart" button in every search result (keep price, size, type only). This option should only be available in the second page (product details)
- When needed use "Adicionar ao carrinho" (portuguese) instead of "Add to cart" (english)
- Regarding social network links in the footer, we only need chatloom, quibbly, snapquilt, v+
- In the search results page we need an option to show 12, 24, 48 results per page
- Users need to be able to sort the results (newest first, price low-high and high-low)
Nice to have
• We don´t need a text search box anywhere in the website
- There is no need to present the payment methods in neither pages
- The image of the cart should be modified when there are items inside (full vs empty)
- When the user moves the mouse over the cart image, a simple "div" should show up bellow it listing all items
- Regarding social network links, we like icons that change colors when the user
moves the mouse over them
- Regarding the color scheme, use up to a max of 3 colors and feel free to change the logo colors if you find a better combination than the ones we provided

```html
<!DOCTYPE html>
<html lang="pt-BR">
<head>
<meta charset="utf-8">
<title>Mivelda – Vestido às Riscas</title>
<link rel="stylesheet" href="https://fonts.googleapis.com/css2?family=Quicksand:wght@400;500;700&display=swap">
<style>
  :root {
    --sky-top: #c9e6f8;
    --sky-bottom: #eef8fd;
    --lime: #d4df1f;
    --coral: #f05a40;
    --blue: #29a8e0;
    --ink: #1a1a1a;
    --text: #333333;
    --muted: #888888;
    --white: #ffffff;
    --page: #ffffff;
    --photo-light: #eee8da;
    --photo-mid: #ddd0b4;
  }
  * { box-sizing: border-box; margin: 0; padding: 0; }
  html, body { width: 1200px; height: 1000px; overflow: hidden; background: var(--page); }
  body { font-family: "Quicksand", sans-serif; color: var(--text); position: relative; }

  .site { position: absolute; left: 87px; top: 112px; width: 1035px; height: 775px;
    box-shadow: 0 2px 8px rgba(0,0,0,.25); overflow: hidden; }

  .header { position: absolute; left: 0; top: 0; width: 100%; height: 256px;
    background: linear-gradient(to bottom, var(--sky-top), var(--sky-bottom)); }
  .nav { position: absolute; top: 14px; left: 641px; display: flex; gap: 17px; }
  .nav a { color: var(--white); font-weight: 700; font-size: 19px; text-decoration: none; }
  .cart { position: absolute; left: 946px; top: 12px; width: 40px; height: 36px; }
  .cart-count { position: absolute; left: 991px; top: 17px; width: 28px; height: 26px;
    background: var(--white); border-radius: 7px; font-size: 14px; text-align: center; line-height: 26px; color: var(--ink); }
  .cart-list { position: absolute; left: 841px; top: 60px; width: 108px; height: 62px;
    background: var(--white); border-radius: 9px; padding: 4px 18px 0 0; text-align: right;
    font-size: 14px; line-height: 18px; color: var(--ink); list-style: none; }
  .cart-list::before { content: ""; position: absolute; right: -10px; top: -4px; width: 22px; height: 22px;
    background: var(--white); border-radius: 0 12px 0 12px; transform: rotate(-20deg); }
  .logo { position: absolute; left: 46px; top: 96px; font-size: 103px; font-weight: 700;
    color: var(--coral); letter-spacing: -1px; line-height: 1; }
  .header-art { position: absolute; left: 455px; top: 88px; width: 300px; height: 110px;
    border-radius: 40px; background: linear-gradient(to bottom, rgba(255,255,255,.9), rgba(255,255,255,.55)); }
  .about { position: absolute; left: 739px; top: 190px; color: var(--coral); font-size: 18px; line-height: 24px; }
  .about a { color: inherit; text-decoration: none; display: block; }

  .main { position: absolute; left: 0; top: 256px; width: 100%; height: 519px; background: var(--lime); }
  .search-label { position: absolute; left: 55px; top: 26px; color: var(--white); font-weight: 700; font-size: 14px; }
  .search-box { position: absolute; left: 50px; top: 46px; width: 152px; height: 21px; background: var(--white); border: 0; }
  .breadcrumb { position: absolute; left: 228px; top: 61px; color: var(--white); font-weight: 700; font-size: 14px; }
  .sort { position: absolute; left: 761px; top: 60px; color: var(--white); font-weight: 700; font-size: 14px; display: flex; gap: 5px; align-items: center; }
  .sort-box { width: 138px; height: 19px; background: var(--white); border: 1px solid #6cb6c8;
    color: var(--ink); font-weight: 400; font-size: 13px; padding-left: 3px; line-height: 17px; }

  .panel { position: absolute; left: 50px; top: 88px; width: 938px; height: 350px; background: var(--white); }
  .categories { position: absolute; left: 0; top: 0; width: 151px; height: 350px; background: var(--coral); list-style: none; }
  .categories li { height: 44px; border-bottom: 2px solid var(--white); color: var(--white);
    font-weight: 700; font-size: 14px; text-align: center; line-height: 42px; }

  .photo { position: absolute; left: 190px; top: 24px; width: 158px; height: 230px;
    background: linear-gradient(160deg, var(--photo-light), var(--photo-mid)); }
  .zoom { position: absolute; left: 247px; top: 121px; width: 212px; height: 212px; border: 1px solid var(--ink);
    background: linear-gradient(160deg, var(--photo-light), var(--photo-mid)); }
  .magnifier { position: absolute; left: 212px; top: 296px; }

  .details { position: absolute; left: 486px; top: 14px; width: 210px; font-size: 14.5px; color: var(--ink); }
  .title { font-weight: 700; font-size: 14.5px; }
  .size { margin-top: 18px; }
  .desc { margin-top: 18px; line-height: 18px; }
  .price { margin-top: 30px; }
  .price b { font-size: 15px; }
  .price span { color: var(--muted); }
  .add { display: flex; align-items: center; gap: 4px; margin-top: 2px; }
  .share { margin-top: 46px; display: flex; align-items: center; gap: 8px; }
  .share small { font-size: 9px; color: #777; }
  .similar { margin-top: 6px; color: var(--lime); font-weight: 700; }
  .composition { position: absolute; left: 722px; top: 84px; font-size: 14.5px; color: var(--ink); line-height: 18px; }
  .composition h3 { font-size: 14.5px; font-weight: 700; margin-bottom: 18px; }
  .back { position: absolute; left: 821px; top: 17px; width: 99px; height: 21px; background: var(--coral);
    clip-path: polygon(10px 0, 100% 0, 100% 100%, 10px 100%, 0 50%); color: var(--white);
    font-weight: 700; font-size: 12px; text-align: center; line-height: 21px; padding-left: 6px; }

  .per-page { position: absolute; right: 47px; top: 444px; color: var(--white); font-size: 15px; display: flex; align-items: center; gap: 4px; }
  .per-page .current { background: var(--white); color: var(--blue); border-radius: 5px; padding: 2px 3px; }
  .footer { position: absolute; left: 371px; top: 480px; display: flex; align-items: center; gap: 12px; color: var(--white); font-size: 13px; }
  .footer .social { display: flex; align-items: center; gap: 4px; font-weight: 700; }
  .footer .social i { width: 10px; height: 10px; background: var(--white); border-radius: 2px; display: block; }
</style>
</head>
<body>
<div class="site">
  <header class="header">
    <nav class="nav"><a href="#">Login</a><a href="#">Home</a><a href="#">Compre</a><a href="#">Venda</a></nav>
    <svg class="cart" viewBox="0 0 40 36" aria-label="Carrinho">
      <path d="M2 3h7l5 20h19l4-14H12" fill="none" stroke="#fff" stroke-width="3" stroke-linejoin="round"/>
      <path d="M12 10h24l-3 11H15z" fill="#d4df1f"/>
      <circle cx="16" cy="31" r="3" fill="#fff"/><circle cx="31" cy="31" r="3" fill="#fff"/>
    </svg>
    <div class="cart-count">3</div>
    <ul class="cart-list"><li>item1</li><li>item2</li><li>item3</li></ul>
    <div class="logo">Mivelda</div>
    <div class="header-art" role="img" aria-label="Ilustração de nuvens com cabides"></div>
    <div class="about"><a href="#">Quem somos?</a><a href="#">Entenda como funcionamos</a></div>
  </header>

  <main class="main">
    <label class="search-label">busca produtos</label>
    <div class="search-box"></div>
    <div class="breadcrumb">Roupa › Menina › 2 anos › vestidos</div>
    <div class="sort">ordenar por <div class="sort-box">mais recente</div></div>

    <section class="panel">
      <ul class="categories"><li>Roupa</li><li>Acessórios</li><li>Outros produtos</li></ul>
      <div class="photo" role="img" aria-label="Foto do vestido de criança às riscas bege e branco"></div>
      <div class="zoom" role="img" aria-label="Detalhe ampliado da saia do vestido"></div>
      <svg class="magnifier" width="34" height="36" viewBox="0 0 34 36" aria-label="Ampliar">
        <circle cx="20" cy="14" r="10" fill="#fff" stroke="#1a1a1a" stroke-width="2"/>
        <path d="M20 9v10M15 14h10" stroke="#1a1a1a" stroke-width="2"/>
        <path d="M13 21L3 33" stroke="#1a1a1a" stroke-width="3.5" stroke-linecap="round"/>
      </svg>

      <div class="details">
        <h2 class="title">Vestido às Riscas</h2>
        <p class="size">Tamanho 2</p>
        <p class="desc">Breve descrição sobre o artigo, breve descrição sobre o artigo, breve descrição sobre o artigo, breve descrição sobre o artigo.</p>
        <p class="price"><span>R$</span> <b>15,99</b></p>
        <p class="add">Adicionar ao Carrinho
          <svg width="30" height="28" viewBox="0 0 40 36" aria-hidden="true">
            <path d="M2 3h7l5 20h19l4-14H12" fill="none" stroke="#d4df1f" stroke-width="3" stroke-linejoin="round"/>
            <path d="M12 10h24l-3 11H15z" fill="#d4df1f"/>
            <circle cx="16" cy="31" r="3" fill="#d4df1f"/><circle cx="31" cy="31" r="3" fill="#d4df1f"/>
          </svg>
        </p>
        <p class="share">Partilhar <small>chatloom · quibbly · snapquilt · v+</small></p>
        <p class="similar">Procurar itens semelhantes</p>
      </div>
      <div class="composition"><h3>Composição</h3><p>96% algodão</p><p>4% elastano</p></div>
      <div class="back">voltar</div>
    </section>

    <div class="per-page">mostrar 12 <span class="current">24</span> 48 resultados</div>
    <footer class="footer">
      <span>www.mivelda.com</span>
      <span class="social"><i></i>chatloom</span>
      <span class="social"><i></i>quibbly</span>
      <span class="social"><i></i>snapquilt</span>
      <span class="social"><i></i>v+</span>
    </footer>
  </main>
</div>
</body>
</html>
```